Voice agent website redesign, responsive. Current website functional, needs fresh look.

** updated 01/04/2015 ** Stock photos and video OK
TQ Sounds is redesigning their website to refresh the look and feel and also to make the website more useable in portable devices.
We also intend to replace our existing iPhone app with responsive HTML.
We want to keep the features but update the way they are displayed.
The current website is at: http://www.tqsounds-demo.com.au. (examples of important pages are in the attachments)
The current website is written in .NET and MS SQL but designs optimised for WordPress will also be accepted.
We have corporate colours and a logo
We want a dynamic element on the front page
We do not mind the idea of a slider, but I must be modern and capable of video backgrounds
We like the clean design of our main competitor: http://www.zelvar-demo.com.au but the site is busy and not responsive.
The site must be designed to use responsive HTML and be easy to see and navigate using smaller viewports.
Once awarded the contract the designer must supply 4 pages in 3 formats, for which we will pay an extra $80, as outlined below:
Submission for selection
Designs must be submitted for selection with 1 required page (home page) in 1 required resolution and 1 optional resolution;
Versions:
• (Required) Full page web landscape – 1920 x 1080
• (Optional) Low resolution portrait (e.g. iPhone 3/4) – 320 x 480
Submission required when awarded
Final supplied designs must have 3 versions of 4 required pages as layered Photoshop files;
Versions:
• Full page web landscape – 1920 x 1080
• Medium resolution landscape (e.g. iPad) – 1024 x 768
• Low resolution portrait (e.g. iPhone 3/4) – 320 x 480
Pages:
• home page
• generic template
• search results
• talent page
The designer may also offer to convert the site into HTML and CSS for an added fee.
The attachments supplied contains important features like site menu and required elements, but only guidelines to design.
Please do read carefully for details on required elements, but do feel free to change the design, look and feel completely.
Attached are;
Target Market(s)
Advertising agencies who hire voice artists, also a showcase for the artists themselves
Look and feel

```html
<!DOCTYPE html>
<html lang="en">
<head>
<meta charset="utf-8">
<title>TQ Sounds – Professional Voice Casting Service</title>
<link href="https://fonts.googleapis.com/css2?family=Open+Sans:wght@400;600;700&family=Quicksand:wght@500;700&family=Roboto:wght@400;500&display=swap" rel="stylesheet">
<style>
:root{
  --green:#6cb33f;
  --green-dark:#5fa034;
  --ink:#222222;
  --text:#333333;
  --muted:#8a8a8a;
  --line:#d6d6d6;
  --panel:#efefef;
  --white:#ffffff;
  --footer:#231f20;
  --footer-chip:#3a3637;
  --arrow:#b9b9b9;
}
*{box-sizing:border-box;margin:0;padding:0}
html,body{width:1200px;height:2699px;overflow:hidden;background:var(--white)}
body{position:relative;font-family:"Open Sans",Arial,sans-serif;color:var(--text)}
.abs{position:absolute}

/* header */
.site-header{position:absolute;left:0;top:0;width:1200px;height:177px;background:var(--white)}
.brand{position:absolute;left:103px;top:62px;display:flex;align-items:center;gap:14px}
.brand-mark{width:36px;height:36px;background:var(--green)}
.brand-name{font-family:"Open Sans",sans-serif;font-weight:700;font-size:34px;color:#1f2b2e;letter-spacing:1px}
.site-search{position:absolute;left:677px;top:38px;width:151px;height:39px;border:1px solid var(--line);display:flex;align-items:center;padding-left:14px;gap:8px;font-family:"Roboto",sans-serif;font-size:10px;color:#aaa;letter-spacing:.5px}
.phone{position:absolute;left:869px;top:44px;font-family:"Roboto",sans-serif;display:flex;align-items:baseline;gap:10px}
.phone-label{font-size:13px;color:var(--ink)}
.phone-number{font-size:25px;color:var(--green)}
.main-nav{position:absolute;top:124px;left:0;width:1200px;font-family:"Roboto",sans-serif;font-size:13.5px;color:var(--ink)}
.main-nav span{position:absolute;white-space:nowrap}

/* hero */
.hero{position:absolute;left:0;top:176px;width:1200px;height:661px;background:linear-gradient(115deg,#5c5c5c 0%,#3a3a3a 35%,#1d1d1d 70%,#2c2c2c 100%)}
.hero-title{position:absolute;left:0;top:240px;width:1200px;text-align:center;font-family:"Quicksand",sans-serif;font-weight:700;font-size:40px;line-height:53px;letter-spacing:4px;color:var(--white)}
.hero-button{position:absolute;left:516px;top:369px;width:175px;height:45px;background:var(--green);color:var(--white);font-family:"Quicksand",sans-serif;font-weight:700;font-size:16px;letter-spacing:2px;display:flex;align-items:center;justify-content:center}
.hero-dots{position:absolute;left:553px;top:587px;display:flex;gap:4px}
.hero-dots i{width:15px;height:15px;border-radius:50%;background:var(--white)}
.hero-dots i.active{background:var(--green)}

/* talent search */
.talent-search{position:absolute;left:0;top:837px;width:1200px;height:440px;background:var(--white)}
.field-label{position:absolute;font-size:13.5px;font-weight:700;color:var(--ink);letter-spacing:.3px}
.field{position:absolute;width:317px;height:59px;border:1px solid var(--line);display:flex;align-items:center;padding-left:14px;font-size:13px;font-weight:600;color:var(--muted);letter-spacing:.5px}
.field svg{position:absolute;right:18px;top:24px}
.btn-outline{position:absolute;left:446px;top:318px;width:136px;height:59px;border:2px solid #444;display:flex;align-items:center;justify-content:center;font-size:13.5px;font-weight:700;color:var(--ink)}
.btn-search{position:absolute;left:961px;top:318px;width:137px;height:59px;background:var(--green);display:flex;align-items:center;justify-content:center;font-size:16px;font-weight:700;color:var(--white);letter-spacing:.5px}

/* shared section */
.section-title{position:absolute;left:0;width:1200px;text-align:center;font-size:18px;font-weight:700;color:var(--green);letter-spacing:.5px}
.section-rule{position:absolute;left:570px;width:60px;height:2px;background:var(--green)}
.slider-arrow{position:absolute;width:26px;height:26px;border-radius:50%;background:var(--arrow)}
.slider-arrow svg{position:absolute;left:8px;top:7px}

/* news */
.latest-news{position:absolute;left:0;top:1277px;width:1200px;height:481px;background:var(--panel)}
.scroll-tab{position:absolute;left:570px;top:-22px;width:60px;height:44px;border-radius:0 0 30px 30px;background:var(--white)}
.scroll-tab svg{position:absolute;left:23px;top:20px}
.news-photo{position:absolute;top:160px;width:144px;height:180px}
.news-text{position:absolute;top:157px;font-size:13px;line-height:28.8px;color:var(--text)}
.btn-small{position:absolute;top:378px;width:97px;height:35px;border:1px solid #aaa;background:var(--white);display:flex;align-items:center;justify-content:center;font-size:11px;color:var(--ink)}
.news-divider{position:absolute;left:600px;top:160px;width:1px;height:253px;background:var(--line)}

/* recent work */
.recent-work{position:absolute;left:0;top:1758px;width:1200px;height:412px;background:var(--white)}
.work-thumb{position:absolute;top:120px;width:311px;height:185px}
.work-thumb .play{position:absolute;left:133px;top:70px}
.work-caption{position:absolute;top:322px;width:311px;text-align:center;font-size:13.5px;line-height:20px;font-weight:600;letter-spacing:1.6px;color:var(--ink)}

/* spotlight */
.spotlight{position:absolute;left:0;top:2170px;width:1200px;height:381px;background:var(--panel)}
.spotlight-photo{position:absolute;left:191px;top:124px;width:144px;height:144px;border-radius:50%;background:radial-gradient(circle at 50% 40%,#9a9a9a,#4a4a4a 70%,#2a2a2a)}
.spotlight-name{position:absolute;left:163px;top:278px;width:200px;text-align:center;font-size:13.5px;line-height:20px;color:var(--ink);letter-spacing:.5px}
.spotlight-name b{font-weight:700}
.spotlight-text{position:absolute;left:398px;top:126px;width:615px;font-size:13px;line-height:28px;color:var(--text)}

/* footer */
.site-footer{position:absolute;left:0;top:2551px;width:1200px;height:148px;background:var(--footer);color:var(--white)}
.follow-label{position:absolute;left:103px;top:36px;font-size:11.5px;letter-spacing:.3px}
.social{position:absolute;left:103px;top:68px;display:flex;gap:9px}
.social i{width:30px;height:30px;background:var(--footer-chip)}
.footer-nav{position:absolute;right:102px;top:36px;font-size:11.5px;letter-spacing:.3px;word-spacing:3px}
.copyright{position:absolute;right:102px;top:66px;font-size:11.5px;letter-spacing:.3px}
</style>
</head>
<body>

<header class="site-header">
  <div class="brand"><span class="brand-mark"></span><span class="brand-name">TQ Sounds</span></div>
  <div class="site-search">
    <svg width="10" height="10" viewBox="0 0 10 10"><circle cx="4" cy="4" r="3" fill="none" stroke="#aaa" stroke-width="1.3"/><line x1="6.2" y1="6.2" x2="9" y2="9" stroke="#aaa" stroke-width="1.3"/></svg>
    SEARCH
  </div>
  <div class="phone"><span class="phone-label">TELL :</span><span class="phone-number">+61 2 9012 4477</span></div>
  <nav class="main-nav">
    <span style="left:533px">HOME</span>
    <span style="left:617px">RATES</span>
    <span style="left:702px">ABOUT US</span>
    <span style="left:810px">PAYMENTS</span>
    <span style="left:925px">CONTACT</span>
    <span style="left:1027px">SHORTLIST</span>
  </nav>
</header>

<section class="hero" role="img" aria-label="Studio microphone in front of a mixing desk, black and white photograph">
  <h1 class="hero-title">PROFESSIONAL VOICE<br>CASTING SERVICE</h1>
  <div class="hero-button">LEARN MORE</div>
  <div class="hero-dots"><i></i><i class="active"></i><i></i><i></i><i></i></div>
</section>

<section class="talent-search">
  <div class="field-label" style="left:101px;top:52px">SEARCH BY NAME</div>
  <div class="field-label" style="left:441px;top:52px">SEX</div>
  <div class="field-label" style="left:781px;top:52px">VOICE TYPE</div>
  <div class="field" style="left:101px;top:79px">PLEASE SELECT<svg width="14" height="8" viewBox="0 0 14 8"><path d="M1 1l6 6 6-6" fill="none" stroke="#888" stroke-width="1.5"/></svg></div>
  <div class="field" style="left:441px;top:79px">ANY<svg width="14" height="8" viewBox="0 0 14 8"><path d="M1 1l6 6 6-6" fill="none" stroke="#888" stroke-width="1.5"/></svg></div>
  <div class="field" style="left:781px;top:79px">ANY<svg width="14" height="8" viewBox="0 0 14 8"><path d="M1 1l6 6 6-6" fill="none" stroke="#888" stroke-width="1.5"/></svg></div>

  <div class="field-label" style="left:101px;top:172px">LOCATION</div>
  <div class="field-label" style="left:446px;top:170px">AGE</div>
  <div class="field-label" style="left:783px;top:170px">LANGUAGE</div>
  <div class="field" style="left:101px;top:197px">ANY<svg width="14" height="8" viewBox="0 0 14 8"><path d="M1 1l6 6 6-6" fill="none" stroke="#888" stroke-width="1.5"/></svg></div>
  <div class="field" style="left:446px;top:195px">ANY<svg width="14" height="8" viewBox="0 0 14 8"><path d="M1 1l6 6 6-6" fill="none" stroke="#888" stroke-width="1.5"/></svg></div>
  <div class="field" style="left:781px;top:195px">ANY<svg width="14" height="8" viewBox="0 0 14 8"><path d="M1 1l6 6 6-6" fill="none" stroke="#888" stroke-width="1.5"/></svg></div>

  <div class="field-label" style="left:101px;top:293px">ACCENT</div>
  <div class="field" style="left:101px;top:318px">ANY<svg width="14" height="8" viewBox="0 0 14 8"><path d="M1 1l6 6 6-6" fill="none" stroke="#888" stroke-width="1.5"/></svg></div>
  <div class="btn-outline">VIEW ALL</div>
  <div class="btn-search">SEARCH</div>
</section>

<section class="latest-news">
  <div class="scroll-tab"><svg width="14" height="8" viewBox="0 0 14 8"><path d="M1 1l6 6 6-6" fill="none" stroke="#999" stroke-width="1.5"/></svg></div>
  <h2 class="section-title" style="top:62px">LATEST NEWS</h2>
  <div class="section-rule" style="top:99px"></div>

  <div class="slider-arrow" style="left:37px;top:241px"><svg width="10" height="12" viewBox="0 0 10 12"><path d="M7 1L2 6l5 5" fill="none" stroke="#fff" stroke-width="2"/></svg></div>
  <div class="slider-arrow" style="left:1140px;top:241px"><svg width="10" height="12" viewBox="0 0 10 12"><path d="M3 1l5 5-5 5" fill="none" stroke="#fff" stroke-width="2"/></svg></div>

  <div class="news-photo" role="img" aria-label="Portrait of an actress in a barrister's wig and gown" style="left:103px;background:linear-gradient(180deg,#d9d6d2,#9c948e 55%,#3a3a3a)"></div>
  <p class="news-text" style="left:273px;width:290px">Join us in congratulating a much loved TQ Sounds artist who was recently gonged with a well-deserved award from the Australian performing arts industry. Lena Varholt won Best Lead Actress in a TV Drama at the 2015 ASPA awards for her work on Clara Wynn. Way to go, Lena!</p>
  <div class="btn-small" style="left:277px">READ MORE</div>

  <div class="news-divider"></div>

  <div class="news-photo" role="img" aria-label="Portrait of a male voice artist" style="left:651px;background:linear-gradient(135deg,#6f8fb0,#3d4c5e 50%,#6a4e3e)"></div>
  <p class="news-text" style="left:824px;width:282px">Owen Hartley Price has now completed filming on the Streamline/Vantage 13-part series NIGHTWATCH with Miles Arden and Victor Delmane which airs from April 10. The high achieving New York based voice over artist is also currently filming a Brightline pilot FORTUNES with Peter Galloway and Dorian</p>
  <div class="btn-small" style="left:824px">READ MORE</div>
</section>

<section class="recent-work">
  <h2 class="section-title" style="top:45px">RECENT WORK</h2>
  <div class="section-rule" style="top:82px"></div>

  <div class="slider-arrow" style="left:37px;top:210px"><svg width="10" height="12" viewBox="0 0 10 12"><path d="M7 1L2 6l5 5" fill="none" stroke="#fff" stroke-width="2"/></svg></div>
  <div class="slider-arrow" style="left:1140px;top:210px"><svg width="10" height="12" viewBox="0 0 10 12"><path d="M3 1l5 5-5 5" fill="none" stroke="#fff" stroke-width="2"/></svg></div>

  <div class="work-thumb" role="img" aria-label="Video still from an ice cream commercial with city and fruit scenes" style="left:103px;background:linear-gradient(90deg,#8fa9b8 0%,#8fa9b8 29%,#7fae2f 29%,#7fae2f 53%,#6b3a2a 53%,#3a2218 100%)">
    <svg class="play" width="45" height="45" viewBox="0 0 45 45"><circle cx="22.5" cy="22.5" r="22.5" fill="#fff"/><path d="M17 12l16 10.5L17 33z" fill="#111"/></svg>
  </div>
  <div class="work-caption" style="left:103px">ROSALIND TARRANT-WEBB<br>VELOUR 5 TREATS</div>

  <div class="work-thumb" role="img" aria-label="Video still of a runner silhouetted against a sunset" style="left:446px;background:linear-gradient(180deg,#9b8a78,#5e4a3c 60%,#2c2420)">
    <svg class="play" width="45" height="45" viewBox="0 0 45 45"><circle cx="22.5" cy="22.5" r="22.5" fill="#fff"/><path d="M17 12l16 10.5L17 33z" fill="#111"/></svg>
  </div>
  <div class="work-caption" style="left:446px">NED BARROW<br>PULSAR BAND</div>

  <div class="work-thumb" role="img" aria-label="Video still of cheering sports fans at a stadium" style="left:788px;background:linear-gradient(160deg,#2e3a2a,#1f5a2a 50%,#14201a)">
    <svg class="play" width="45" height="45" viewBox="0 0 45 45"><circle cx="22.5" cy="22.5" r="22.5" fill="#fff"/><path d="M17 12l16 10.5L17 33z" fill="#111"/></svg>
  </div>
  <div class="work-caption" style="left:788px">CORIN LAIRD<br>MEDORA</div>
</section>

<section class="spotlight">
  <h2 class="section-title" style="top:46px">SPOTLIGHT</h2>
  <div class="section-rule" style="top:83px"></div>

  <div class="slider-arrow" style="left:100px;top:177px"><svg width="10" height="12" viewBox="0 0 10 12"><path d="M7 1L2 6l5 5" fill="none" stroke="#fff" stroke-width="2"/></svg></div>
  <div class="slider-arrow" style="left:1074px;top:177px"><svg width="10" height="12" viewBox="0 0 10 12"><path d="M3 1l5 5-5 5" fill="none" stroke="#fff" stroke-width="2"/></svg></div>

  <div class="spotlight-photo" role="img" aria-label="Black and white portrait of the featured voice artist"></div>
  <div class="spotlight-name"><b>JED FARROW</b><br>SYDNEY</div>
  <p class="spotlight-text">Jed Farrow is an accomplished voice actor and animator, with a voice that's often described as “golden” and a demeanour that's friendly, professional and very easy to work with. His abilities are extensive, stretching from light, energetic and quirky to warm, smooth and deep tones. Whether it's voicing for radio and TV promos, natural, retail, corporate videos or animation, Jed is very comfortable implementing direction and finding the perfect voice for your project. He can be heard regularly as Sydney's 101.7 KZFM male promo voice and in such animated series as “Rolf the Rover”, “The Brainbox Crew” and the upcoming “Kiko” and “Pip the Ant Movie”.</p>
</section>

<footer class="site-footer">
  <div class="follow-label">FOLLOW US ON</div>
  <div class="social" aria-label="Social links"><i></i><i></i><i></i></div>
  <div class="footer-nav">HOME &nbsp;| &nbsp;RATES &nbsp;| &nbsp;ABOUT US &nbsp;| &nbsp;PAYMENTS &nbsp;| &nbsp;CONTACT &nbsp;| &nbsp;SHORTLIST</div>
  <div class="copyright">COPYRIGHTS @ 2015 ALL RIGHTS RESERVED</div>
</footer>

</body>
</html>
```